Redesign of Smart Watch Gift Voucher-SEE ATTACHED CURRENT DESIGN

I need to redesign my existing design using all same content and elements.

MY ENVISION: I invision more of a professional advertisement type of flyer/voucher. Imagine how Corvel.com would create a professionally looking flyer promoting the lumo or veno.

you can get many ideas about professional design by looking at some of corvels flyer designs :
https://www.findora-example.net/search?q=lumo+advertisment&mode=img&ref=a83kd02mzq7

stock photos are attached, you do not have to use them all, you can use some or none i am open to your designs using your own images if you want...just make sure the smartwatch looks black

DO NOT LEAVE ANY CONTENT OR ELEMENTS OUT ON MOCK UP PLEASE

SEE ATTACHED CURRENT DESIGN

I need to redesign my existing design using all same content and elements. DO NOT LEAVE ANY CONTENT OR ELEMENTS OUT ON MOCK UP PLEASE

Target Market(s)

B2B-you can get many ideas about professional design by looking at some of corvels flyer designs :

Industry/Entity Type

Marketing

Requirements
Must have
• I need to redesign my existing design using all same content and elements. DO NOT LEAVE ANY CONTENT OR ELEMENTS OUT ON MOCK UP PLEASE

Nice to have

Should not have

```html
<!DOCTYPE html>
<html lang="en">
<head>
<meta charset="utf-8">
<title>Smartwatch Reward Flyer</title>
<link rel="stylesheet" href="https://fonts.googleapis.com/css2?family=Jost:wght@200;300;400;500&display=swap">
<style>
  :root {
    --stage: #b3b3b3;
    --paper: #0c0c0d;
    --red: #d1161e;
    --band: #a8141b;
    --white: #f4f4f4;
    --grey: #bdbdbd;
  }
  * { margin: 0; padding: 0; box-sizing: border-box; }
  html, body { width: 1070px; height: 1200px; overflow: hidden; }
  body { background: var(--stage); font-family: "Jost", sans-serif; color: var(--white); }

  .flyer { position: absolute; left: 80px; top: 0; width: 910px; height: 1200px; background: var(--paper); }

  .hero-title { position: absolute; top: 68px; width: 100%; text-align: center; font-weight: 200; font-size: 88px; letter-spacing: 2px; line-height: 1; }
  .hero-sub { position: absolute; top: 170px; width: 100%; text-align: center; color: var(--red); font-weight: 300; font-size: 29px; letter-spacing: 0.5px; }

  .side-heading { color: var(--red); font-weight: 300; font-size: 24px; line-height: 29px; letter-spacing: 0.5px; text-transform: uppercase; }
  .story { position: absolute; left: 47px; top: 312px; width: 192px; }
  .story p { margin-top: 16px; font-size: 10.6px; line-height: 12.7px; color: var(--grey); font-weight: 300; }
  .testimonial { position: absolute; left: 47px; top: 595px; width: 192px; }
  .testimonial blockquote { margin-top: 12px; font-size: 10.6px; line-height: 12.7px; color: var(--grey); font-weight: 300; }
  .testimonial cite { display: block; margin-top: 14px; font-style: normal; font-size: 10.5px; font-weight: 500; color: var(--red); letter-spacing: 0.3px; }

  .product-photo { position: absolute; left: 334px; top: 299px; width: 243px; height: 447px; border-radius: 38px;
    background: radial-gradient(ellipse at 50% 45%, #6b3a1c 0%, #241a15 28%, #161617 45%, #0f0f10 100%); }

  .features { position: absolute; left: 704px; top: 314px; width: 190px; }
  .features ul { list-style: none; margin-top: 22px; }
  .features li { display: flex; align-items: center; height: 30.3px; font-size: 12.2px; font-weight: 300; color: var(--grey); }
  .features svg { width: 10px; height: 10px; margin-right: 8px; flex: none; }

  .tagline { position: absolute; top: 838px; width: 100%; text-align: center; color: var(--red); font-weight: 300; font-size: 35px; line-height: 44px; letter-spacing: 0.6px; }
  .offer-copy { position: absolute; top: 935px; left: 100px; width: 710px; text-align: center; font-size: 11.8px; line-height: 14.6px; color: var(--grey); font-weight: 300; }

  .voucher { position: absolute; left: 53px; top: 1035px; width: 803px; height: 119px; background: var(--band); overflow: hidden; }
  .voucher-photo { position: absolute; inset: 0; clip-path: polygon(450px 0, 803px 0, 803px 119px, 502px 119px);
    background: linear-gradient(90deg, #d8b6a2 0%, #c9a08a 45%, #3b3d44 75%, #6f7278 100%); }
  .voucher-meta { position: absolute; left: 27px; top: 22px; font-size: 12px; line-height: 15px; font-weight: 300; }
  .voucher-meta strong { display: block; font-weight: 500; }
  .voucher-meta .expiry { margin-top: 20px; }
  .voucher-rule { position: absolute; left: 140px; width: 1px; background: rgba(255,255,255,0.6); }
  .voucher-redeem { position: absolute; left: 159px; top: 22px; font-size: 12px; line-height: 16px; font-weight: 300; text-transform: uppercase; }
  .voucher-redeem .url { margin-top: 18px; font-weight: 500; font-size: 12.8px; letter-spacing: 0.3px; }
  .voucher-redeem .terms { font-size: 9px; line-height: 12px; }
</style>
</head>
<body>
  <main class="flyer">
    <h1 class="hero-title">ENJOY</h1>
    <p class="hero-sub">Your Brand New Smartwatch</p>

    <section class="story">
      <h2 class="side-heading">How can we<br>do this?</h2>
      <p>We Have A Couple Retial Parters That We Team Up With To "Crowd Purchase" Huge Shipping Containers That Hold 10's Of Thousands Of Electronic Products At 80-90% Off Retail. We Simply Pass Our Savings On To You As We Do Not Profit From Our Electronic Products. You Are Basically Able To "Piggy Back" On Our Parternships And Buying Power To Get An Attractive Electronic Preminum For A Fraction Of The Retail Cost.</p>
    </section>

    <section class="testimonial">
      <h2 class="side-heading">What<br>others say?</h2>
      <blockquote>"Are You Sure This Is Not A Norvia Stellar Smartwatch In Disguise??? I Love Mine".</blockquote>
      <cite>DALE M. BAYVIEW, NJ</cite>
    </section>

    <div class="product-photo" role="img" aria-label="Black smartwatch with a glowing amber flame watch face"></div>

    <section class="features">
      <h2 class="side-heading">Features</h2>
      <ul>
        <li><svg viewBox="0 0 10 10"><circle cx="5" cy="5" r="4.2" fill="none" stroke="var(--red)" stroke-width="1.1"/><path d="M3 5.1l1.5 1.5L7.6 3.4" fill="none" stroke="var(--red)" stroke-width="1.1"/></svg>Pedometer</li>
        <li><svg viewBox="0 0 10 10"><circle cx="5" cy="5" r="4.2" fill="none" stroke="var(--red)" stroke-width="1.1"/><path d="M3 5.1l1.5 1.5L7.6 3.4" fill="none" stroke="var(--red)" stroke-width="1.1"/></svg>Calorie Counter</li>
        <li><svg viewBox="0 0 10 10"><circle cx="5" cy="5" r="4.2" fill="none" stroke="var(--red)" stroke-width="1.1"/><path d="M3 5.1l1.5 1.5L7.6 3.4" fill="none" stroke="var(--red)" stroke-width="1.1"/></svg>Blood Pressure Monitor</li>
        <li><svg viewBox="0 0 10 10"><circle cx="5" cy="5" r="4.2" fill="none" stroke="var(--red)" stroke-width="1.1"/><path d="M3 5.1l1.5 1.5L7.6 3.4" fill="none" stroke="var(--red)" stroke-width="1.1"/></svg>Sleep Monitoring</li>
        <li><svg viewBox="0 0 10 10"><circle cx="5" cy="5" r="4.2" fill="none" stroke="var(--red)" stroke-width="1.1"/><path d="M3 5.1l1.5 1.5L7.6 3.4" fill="none" stroke="var(--red)" stroke-width="1.1"/></svg>Reminders Feature</li>
        <li><svg viewBox="0 0 10 10"><circle cx="5" cy="5" r="4.2" fill="none" stroke="var(--red)" stroke-width="1.1"/><path d="M3 5.1l1.5 1.5L7.6 3.4" fill="none" stroke="var(--red)" stroke-width="1.1"/></svg>Alarm Clock</li>
        <li><svg viewBox="0 0 10 10"><circle cx="5" cy="5" r="4.2" fill="none" stroke="var(--red)" stroke-width="1.1"/><path d="M3 5.1l1.5 1.5L7.6 3.4" fill="none" stroke="var(--red)" stroke-width="1.1"/></svg>Distance Tracker</li>
        <li><svg viewBox="0 0 10 10"><circle cx="5" cy="5" r="4.2" fill="none" stroke="var(--red)" stroke-width="1.1"/><path d="M3 5.1l1.5 1.5L7.6 3.4" fill="none" stroke="var(--red)" stroke-width="1.1"/></svg>Heart Rate Monitor</li>
        <li><svg viewBox="0 0 10 10"><circle cx="5" cy="5" r="4.2" fill="none" stroke="var(--red)" stroke-width="1.1"/><path d="M3 5.1l1.5 1.5L7.6 3.4" fill="none" stroke="var(--red)" stroke-width="1.1"/></svg>Stopwatch</li>
        <li><svg viewBox="0 0 10 10"><circle cx="5" cy="5" r="4.2" fill="none" stroke="var(--red)" stroke-width="1.1"/><path d="M3 5.1l1.5 1.5L7.6 3.4" fill="none" stroke="var(--red)" stroke-width="1.1"/></svg>Phone Locator</li>
        <li><svg viewBox="0 0 10 10"><circle cx="5" cy="5" r="4.2" fill="none" stroke="var(--red)" stroke-width="1.1"/><path d="M3 5.1l1.5 1.5L7.6 3.4" fill="none" stroke="var(--red)" stroke-width="1.1"/></svg>Remote Camera</li>
        <li><svg viewBox="0 0 10 10"><circle cx="5" cy="5" r="4.2" fill="none" stroke="var(--red)" stroke-width="1.1"/><path d="M3 5.1l1.5 1.5L7.6 3.4" fill="none" stroke="var(--red)" stroke-width="1.1"/></svg>Waterproof</li>
      </ul>
    </section>

    <h2 class="tagline">Take Control of your Life with<br>Your New Smart Fitness Watch</h2>
    <p class="offer-copy">Congratulations, you hove been rewarded with a Brand New Smart Fitness Watch shipped right to your door. Just pay shipping and handling. Your new Smart Fitness Watch has these features: Sport Mode, Pedometer, distance calorie,heart rate, blood pressure, stopwatch, sleep monitoring, phone locator, reminders, remote camera, an alarm clock and much more!</p>

    <section class="voucher">
      <div class="voucher-photo" role="img" aria-label="Hand tapping a black smartwatch on a wrist"></div>
      <div class="voucher-meta">
        <span>CERTIFICATE ID</span><strong>91772-89218</strong>
        <div class="expiry"><span>EXPIRES</span><strong>10/03/2020</strong></div>
      </div>
      <span class="voucher-rule" style="top:22px;height:34px"></span>
      <span class="voucher-rule" style="top:68px;height:34px"></span>
      <div class="voucher-redeem">
        <p>View all the details of this<br>special offer and redeem online at</p>
        <p class="url">WWW.PERKSANDPRIZES-EXAMPLE.COM</p>
        <p class="terms">*Terms and conditions apply see website for details</p>
      </div>
    </section>
  </main>
</body>
</html>
```